hobby beef jerky maker looking to break into the commercial market

We need product labels designed for each flavour of jerky we make. Currently have 3 flavours that we are ready to share with the world. We need in your face designs to help us stand out from an already crowded market.
The product name is Rivet Beef Jerky.
The flavours we offer have been named Porch Lope, Ember Glaze and Chili Knack.
The Rivet Beef Jerky Title should remain the same across the three labels but the design for each flavour can change as you see fit.
Label needs to fit within 110mm x 110mm to suit our current packaging

Industry/Entity Type

Food Production

Logo Text

Morvendale Apiary

Colors

Designer to choose colors to be used in the design.

Requirements
Must have
• "Rivet Beef Jerky" font and colour must remain the same across the 3 designs
Nice to have
• The labels will be used on the clear side of the packaging with a small space towards the bottom being left visible so the product inside can be seen

```html
<!DOCTYPE html>
<html lang="en">
<head>
<meta charset="utf-8">
<title>Rivet Beef Jerky – Chili Knack Label</title>
<link rel="stylesheet" href="https://fonts.googleapis.com/css2?family=Oleo+Script:wght@700&display=swap">
<style>
  :root {
    --cream: #ecdcb4;
    --cream-deep: #dccb9f;
    --slate: #5e6a5c;
    --chili: #a01a35;
    --ink: #1f241c;
  }
  html, body {
    margin: 0;
    padding: 0;
    width: 1200px;
    height: 1200px;
    overflow: hidden;
    background: var(--cream);
  }
  .label {
    position: relative;
    width: 1200px;
    height: 1200px;
  }
  .label svg {
    display: block;
  }
  .script {
    font-family: "Oleo Script", "Georgia", serif;
    font-weight: 700;
  }
  .brand-word { fill: var(--slate); }
  .flavour-word {
    fill: var(--cream);
    stroke: var(--slate);
    stroke-width: 14;
    stroke-linejoin: round;
    paint-order: stroke fill;
  }
  .rule-dark { stroke: var(--ink); stroke-width: 2; }
  .rule-red { stroke: var(--chili); stroke-width: 3; }
  .zigzag { fill: none; stroke-width: 5; stroke-linejoin: miter; }
  .zigzag-dark { stroke: var(--ink); }
  .zigzag-red { stroke: var(--chili); }
</style>
</head>
<body>
<main class="label">
  <svg width="1200" height="1200" viewBox="0 0 1200 1200" xmlns="http://www.w3.org/2000/svg">
    <defs>
      <radialGradient id="pattern-tone" cx="50%" cy="50%" r="60%">
        <stop offset="0%" stop-color="var(--cream-deep)"/>
        <stop offset="100%" stop-color="var(--cream)"/>
      </radialGradient>
      <path id="brand-arc" d="M 170 500 Q 600 180 1060 500"/>
    </defs>

    <!-- background ornament area -->
    <rect class="background-pattern" x="0" y="0" width="1200" height="1200" fill="url(#pattern-tone)"
          role="img" aria-label="Faint radial lace mandala pattern"/>

    <!-- frame -->
    <rect class="frame" x="30" y="30" width="1140" height="1140" rx="40"
          fill="none" stroke="var(--slate)" stroke-width="7"/>

    <!-- title rules -->
    <g class="title-rules">
      <line class="rule-dark" x1="128" y1="140" x2="364" y2="140"/>
      <line class="rule-red"  x1="92"  y1="159" x2="364" y2="159"/>
      <line class="rule-dark" x1="128" y1="178" x2="364" y2="178"/>
      <line class="rule-dark" x1="828" y1="140" x2="1068" y2="140"/>
      <line class="rule-red"  x1="828" y1="159" x2="1104" y2="159"/>
      <line class="rule-dark" x1="828" y1="178" x2="1068" y2="178"/>
    </g>

    <!-- brand name -->
    <text class="script brand-word brand-top" x="600" y="200" font-size="132" text-anchor="middle">Rivet</text>
    <text class="script brand-word brand-arc" font-size="118">
      <textPath href="#brand-arc" startOffset="50%" text-anchor="middle">Beef Jerky</textPath>
    </text>

    <!-- chili illustration area -->
    <rect class="chili-illustration" x="110" y="460" width="1000" height="580" rx="270"
          fill="var(--chili)" role="img" aria-label="Cluster of four red chili peppers"/>

    <!-- flavour name -->
    <g class="flavour" transform="rotate(-18 600 890)">
      <text class="script flavour-word" x="520" y="880" font-size="165" text-anchor="middle">Chili</text>
      <text class="script flavour-word" x="700" y="1010" font-size="165" text-anchor="middle">Knack</text>
    </g>

    <!-- bottom zigzag band -->
    <g class="zigzag-band">
      <path class="zigzag zigzag-dark" d="M64 1072 l44.67 16 l44.67 -16 l44.67 16 l44.67 -16 l44.67 16 l44.67 -16 l44.67 16 l44.67 -16 l44.67 16 l44.67 -16 l44.67 16 l44.67 -16 l44.67 16 l44.67 -16 l44.67 16 l44.67 -16 l44.67 16 l44.67 -16 l44.67 16 l44.67 -16 l44.67 16 l44.67 -16 l44.67 16 l44.67 -16"/>
      <path class="zigzag zigzag-red" d="M64 1090 l44.67 16 l44.67 -16 l44.67 16 l44.67 -16 l44.67 16 l44.67 -16 l44.67 16 l44.67 -16 l44.67 16 l44.67 -16 l44.67 16 l44.67 -16 l44.67 16 l44.67 -16 l44.67 16 l44.67 -16 l44.67 16 l44.67 -16 l44.67 16 l44.67 -16 l44.67 16 l44.67 -16 l44.67 16 l44.67 -16"/>
      <path class="zigzag zigzag-dark" d="M64 1108 l44.67 16 l44.67 -16 l44.67 16 l44.67 -16 l44.67 16 l44.67 -16 l44.67 16 l44.67 -16 l44.67 16 l44.67 -16 l44.67 16 l44.67 -16 l44.67 16 l44.67 -16 l44.67 16 l44.67 -16 l44.67 16 l44.67 -16 l44.67 16 l44.67 -16 l44.67 16 l44.67 -16 l44.67 16 l44.67 -16"/>
    </g>
  </svg>
</main>
</body>
</html>
```